Blueprints For A Steady Home Book*

Our book is about using engineering and biblical principles to solve problems in marriage. We are the wedlock Architects. See our branded logo in the attachments. We would like to see different types of graphics that shows continuous improvement in marriage. Our colors should be Gold Black and Red. Could use white text and symbols if needed. Brief description on the back with some quotes and our Picture. Use 5.5x8.5 as the size of the book. Not sure about the spine size.

Target Market(s)

Married couples

Font styles to use
Serif

Colors

Designer to choose colors to be used in the design.

Requirements
Nice to have
• Engineering symbols and Logos.

```html
<!DOCTYPE html>
<html lang="en">
<head>
<meta charset="utf-8">
<title>Blueprints For A Steady Home Book — Cover</title>
<link href="https://fonts.googleapis.com/css2?family=Cinzel:wght@400;500&display=swap" rel="stylesheet">
<style>
  :root {
    --page: #ffffff;
    --board: #0d0d0d;
    --board-edge: #1c1c1c;
    --gold-light: #f3d68a;
    --gold: #c9a24a;
    --gold-deep: #8a6420;
    --gear-orange: #e8632b;
    --gear-teal: #3fa7a0;
    --gear-blue: #5a6fb4;
    --gear-pink: #c8457a;
  }
  * { margin: 0; padding: 0; box-sizing: border-box; }
  html, body {
    width: 1200px;
    height: 1200px;
    overflow: hidden;
    background: var(--page);
  }
  .canvas {
    position: relative;
    width: 1200px;
    height: 1200px;
    background: var(--page);
  }
  .book-cover {
    position: absolute;
    left: 380px;
    top: 260px;
    width: 440px;
    height: 680px;
    background: var(--board);
    overflow: hidden;
  }
  .chalkboard-texture {
    position: absolute;
    inset: 0;
    background: radial-gradient(ellipse at 50% 40%, var(--board-edge) 0%, var(--board) 75%);
  }
  .cover-title {
    position: absolute;
    left: 0;
    right: 0;
    top: 52px;
    text-align: center;
    font-family: "Cinzel", serif;
    font-weight: 400;
    line-height: 1;
    background: linear-gradient(180deg, var(--gold-light) 0%, var(--gold) 45%, var(--gold-deep) 100%);
    -webkit-background-clip: text;
    background-clip: text;
    color: transparent;
  }
  .cover-title .line { display: block; }
  .cover-title .line-1 { font-size: 34px; letter-spacing: 1px; }
  .cover-title .line-2 { font-size: 56px; margin-top: 14px; }
  .cover-title .line-3 { font-size: 62px; margin-top: 10px; }
  .cover-title .line-4 { font-size: 62px; margin-top: 10px; }
  .gear-cluster {
    position: absolute;
    left: 42px;
    top: 345px;
    width: 356px;
    height: 190px;
    border-radius: 48% 48% 50% 50% / 40% 40% 60% 60%;
    background: radial-gradient(circle at 50% 45%, var(--gear-orange) 0%, var(--gear-blue) 40%, var(--gear-teal) 65%, rgba(200,69,122,0.6) 85%, transparent 100%);
    opacity: 0.85;
  }
  .publisher-mark {
    position: absolute;
    left: 0;
    right: 0;
    top: 585px;
    display: flex;
    flex-direction: column;
    align-items: center;
    gap: 8px;
  }
  .publisher-mark .dot {
    width: 26px;
    height: 26px;
    border-radius: 50%;
    background: var(--gold);
  }
  .publisher-mark .name {
    font-family: "Cinzel", serif;
    font-weight: 400;
    font-size: 17px;
    color: var(--gold);
    letter-spacing: 0.5px;
  }
</style>
</head>
<body>
  <div class="canvas">
    <div class="book-cover">
      <div class="chalkboard-texture" role="img" aria-label="Black chalkboard covered with faint handwritten equations and curves"></div>
      <h1 class="cover-title">
        <span class="line line-1">BLUEPRINTS FOR</span>
        <span class="line line-2">A STEADY</span>
        <span class="line line-3">HOME</span>
        <span class="line line-4">BOOK</span>
      </h1>
      <div class="gear-cluster" role="img" aria-label="Heart-shaped cluster of colourful interlocking gears with small icons"></div>
      <div class="publisher-mark">
        <span class="dot"></span>
        <span class="name">the wedlock Architects</span>
      </div>
    </div>
  </div>
</body>
</html>
```